Image Copy

This is one of three images that need to be designed for slides on our Bidzeal landing page. The first slide image background is 713 x 502 and I have included a sample. The copy needs to be designed and it needs to fit more to the left as there are words that on the right, which resize depending on the device. The background is white, use your own discretion for style, color, caps vs lower case etc... A test website is available to view at http://dev.quarnel-systems.test/varlox.html - we are working on the 2nd slide.

```html
<!DOCTYPE html>
<html lang="en">
<head>
<meta charset="utf-8">
<title>Better IT Support</title>
<link rel="stylesheet" href="https://fonts.googleapis.com/css2?family=Mulish:wght@400;700;800&display=swap">
<style>
  :root {
    --red: #e3232c;
    --ink: #111111;
    --grey: #7b7b7b;
    --sand: #e0cdb1;
    --sand-light: #efe3d2;
    --sand-bar: #d8c4a4;
    --paper: #ffffff;
    --paper-warm: #f5efe7;
    --photo-a: #e9e4de;
    --photo-b: #cfd3d6;
  }
  * { margin: 0; padding: 0; box-sizing: border-box; }
  html, body { width: 1200px; height: 844px; overflow: hidden; }
  body { font-family: "Mulish", Arial, sans-serif; background: var(--paper); }
  .slide { position: relative; width: 1200px; height: 844px; overflow: hidden; }
  .backdrop { position: absolute; inset: 0; }
  .headline {
    position: absolute; left: 60px; top: 48px;
    font-size: 55px; font-weight: 800; color: var(--red); letter-spacing: -0.3px;
    line-height: 66px; white-space: nowrap;
  }
  .pitch {
    position: absolute; left: 60px; top: 233px;
    border-left: 6px solid var(--sand-bar);
    padding-left: 22px;
    font-size: 35px; font-weight: 800; line-height: 44px;
    white-space: nowrap;
  }
  .pitch .strong { color: var(--ink); display: block; }
  .pitch .soft { color: var(--grey); display: block; }
  .features { position: absolute; list-style: none; }
  .features.left { left: 60px; top: 642px; }
  .features.right { left: 634px; top: 657px; }
  .feature { position: relative; padding-left: 30px; margin-bottom: 16px; white-space: nowrap; }
  .features.right .feature { margin-bottom: 18px; }
  .feature .tick { position: absolute; left: 0; top: 1px; width: 22px; height: 22px; }
  .feature .title { font-size: 19px; font-weight: 800; color: var(--ink); line-height: 23px; }
  .feature .detail { font-size: 19px; font-weight: 400; color: var(--ink); line-height: 23px; }
</style>
</head>
<body>
<main class="slide">
  <svg class="backdrop" width="1200" height="844" viewBox="0 0 1200 844">
    <defs>
      <linearGradient id="paperFade" x1="0" y1="0" x2="0" y2="1">
        <stop offset="0" stop-color="var(--paper)"/>
        <stop offset="1" stop-color="var(--paper-warm)"/>
      </linearGradient>
      <linearGradient id="photoTone" x1="0" y1="0" x2="1" y2="1">
        <stop offset="0" stop-color="var(--photo-a)"/>
        <stop offset="1" stop-color="var(--photo-b)"/>
      </linearGradient>
    </defs>
    <rect width="1200" height="844" fill="url(#paperFade)"/>
    <path role="img" aria-label="Photo of three smiling laboratory staff in white coats, one holding a report sheet"
          d="M423 95 H1200 V420 C900 560 620 600 423 592 Z" fill="url(#photoTone)"/>
    <path d="M0 574 C300 590 700 600 1200 390 V844 H0 Z" fill="var(--sand-light)"/>
    <path d="M0 600 C350 620 800 610 1200 472 V844 H0 Z" fill="var(--sand)"/>
  </svg>

  <h1 class="headline">You should expert</h1>

  <p class="pitch">
    <span class="strong">GET A BETTER</span>
    <span class="strong">IT&nbsp; SUPPORT</span>
    <span class="strong">SOLUTION</span>
    <span class="soft">for less than you</span>
    <span class="soft">spend now</span>
  </p>

  <ul class="features left">
    <li class="feature">
      <svg class="tick" viewBox="0 0 22 22"><circle cx="11" cy="11" r="9" fill="none" stroke="var(--red)" stroke-width="2"/><path d="M6 11 l4 4 l9 -11" fill="none" stroke="var(--red)" stroke-width="2.6" stroke-linecap="round" stroke-linejoin="round"/></svg>
      <div class="title">“60-second Response”</div>
      <div class="detail">When you need help whether by phone or chat</div>
    </li>
    <li class="feature">
      <svg class="tick" viewBox="0 0 22 22"><circle cx="11" cy="11" r="9" fill="none" stroke="var(--red)" stroke-width="2"/><path d="M6 11 l4 4 l9 -11" fill="none" stroke="var(--red)" stroke-width="2.6" stroke-linecap="round" stroke-linejoin="round"/></svg>
      <div class="title">Business-class Security Suite</div>
      <div class="detail">Not consumer grade or a partial solution</div>
    </li>
    <li class="feature">
      <svg class="tick" viewBox="0 0 22 22"><circle cx="11" cy="11" r="9" fill="none" stroke="var(--red)" stroke-width="2"/><path d="M6 11 l4 4 l9 -11" fill="none" stroke="var(--red)" stroke-width="2.6" stroke-linecap="round" stroke-linejoin="round"/></svg>
      <div class="title">Bullet-proof Backup Solution</div>
      <div class="detail">File &amp; Image, onsite &amp; offsite, versioned and tested</div>
    </li>
  </ul>

  <ul class="features right">
    <li class="feature">
      <svg class="tick" viewBox="0 0 22 22"><circle cx="11" cy="11" r="9" fill="none" stroke="var(--red)" stroke-width="2"/><path d="M6 11 l4 4 l9 -11" fill="none" stroke="var(--red)" stroke-width="2.6" stroke-linecap="round" stroke-linejoin="round"/></svg>
      <div class="title">Monitoring &amp; Management Automation</div>
      <div class="detail">Patch management &amp; sheduling,<br>hardware monitoring, and more...</div>
    </li>
    <li class="feature">
      <svg class="tick" viewBox="0 0 22 22"><circle cx="11" cy="11" r="9" fill="none" stroke="var(--red)" stroke-width="2"/><path d="M6 11 l4 4 l9 -11" fill="none" stroke="var(--red)" stroke-width="2.6" stroke-linecap="round" stroke-linejoin="round"/></svg>
      <div class="title">100% Happiness Guarantee</div>
      <div class="detail">No long-term contracts, no expensive gotchas’<br>- just great service</div>
    </li>
  </ul>
</main>
</body>
</html>
```